Property refurbishment & maintenance Business Card Design

Velmorin Ltd is a leading provider of domestic maintenance, building and refurbishment services. Founded in October 2009 by Piotr Velmorin, we aim to provide our customers with exceptional home improvement and maintenance services whilst minimising the disruption and stress caused.
The building services we provide are of the very highest quality. We provide all of your customers with the peace of mind in knowing that they are dealing with experts in construction, renovation and decoration. This is because we are members of the Guild of Craft Contractors (GCC). We have also had our credentials verified by Surelink and the UK government's Keel Seal scheme.
Target Market(s)
Private home owners,letting agents,tenants
Industry/Entity Type
Home Improvement
Contact Information for Business Card
Velmorin ltd.
Piotr Velmorin
14 Pellham Birch Lane ,Brackwell Cross,Hollshire,BX4 2QR,T.01632318257 M:07924168330
E. info@velmorin.example. www.velmorin.example
Look and feel
Each slider illustrates characteristics of the customer's brand and the style your logo design should communicate.

```html
<!DOCTYPE html>
<html lang="en">
<head>
<meta charset="utf-8">
<title>Velmorin Ltd – Business Card</title>
<link rel="stylesheet" href="https://fonts.googleapis.com/css2?family=PT+Sans:wght@400;700&display=swap">
<style>
  :root {
    --backdrop: #ebe7e1;
    --card-white: #ffffff;
    --slate: #58585a;
    --gold: #c4913f;
    --teal: #3f9a8b;
    --text-light: #ffffff;
  }
  * { margin: 0; padding: 0; box-sizing: border-box; }
  html, body {
    width: 1135px; height: 1200px; overflow: hidden;
    background: var(--backdrop);
    font-family: "PT Sans", Arial, sans-serif;
  }
  .canvas { position: relative; width: 1135px; height: 1200px; }

  .card {
    position: absolute; width: 937px; height: 534px;
    border-radius: 36px; overflow: hidden;
  }
  .card--front { left: 23px; top: 40px; background: var(--card-white); }
  .card--back  { left: 163px; top: 623px; background: var(--gold); }

  .card__swoosh { position: absolute; inset: 0; width: 100%; height: 100%; }

  .brand { position: absolute; line-height: 1; }
  .brand__name { display: block; font-weight: 400; white-space: nowrap; }
  .brand__tagline { display: block; font-weight: 400; white-space: nowrap; }

  .card--front .brand { left: 84px; top: 140px; }
  .card--front .brand__name { font-size: 74px; letter-spacing: 0.13em; color: var(--teal); }
  .card--front .brand__tagline { font-size: 20px; letter-spacing: 0.03em; color: var(--gold); margin-top: 10px; padding-left: 10px; }

  .holder { position: absolute; left: 61px; top: 322px; line-height: 1; }
  .holder__name { font-size: 31px; font-weight: 700; color: var(--slate); }
  .holder__title { font-size: 24px; color: var(--gold); margin-top: 8px; }

  .contact {
    position: absolute; right: 39px; top: 284px;
    list-style: none; text-align: right; color: var(--text-light);
    font-size: 23px; line-height: 1;
  }
  .contact__item { display: flex; justify-content: flex-end; align-items: center; gap: 10px; height: 36px; }
  .contact__icon { width: 20px; height: 20px; fill: var(--text-light); }
  .contact__address { margin-top: 8px; line-height: 38px; }

  .card--back .brand { left: 0; right: 0; top: 228px; text-align: center; }
  .card--back .brand__name { font-size: 104px; letter-spacing: 0.12em; color: var(--text-light); padding-left: 0.12em; }
  .card--back .brand__tagline { font-size: 27px; letter-spacing: 0.03em; color: var(--text-light); margin-top: 12px; }
  .card__web {
    position: absolute; left: 0; right: 0; top: 418px; text-align: center;
    color: var(--text-light); font-size: 27px; letter-spacing: 0.25em;
  }
</style>
</head>
<body>
<div class="canvas">

  <section class="card card--front">
    <svg class="card__swoosh" viewBox="0 0 1049 598" preserveAspectRatio="none" aria-hidden="true">
      <path fill="var(--slate)" d="M1049,22 C880,300 560,525 0,515 L0,598 L1049,598 Z"/>
      <path fill="var(--gold)" d="M0,438 C260,520 540,470 740,328 C560,470 280,540 0,500 Z"/>
    </svg>

    <div class="brand">
      <span class="brand__name">VELMORIN</span>
      <span class="brand__tagline">PROPERTY REFURBISHMENT &amp; MAINTENANCE</span>
    </div>

    <div class="holder">
      <p class="holder__name">Your Name</p>
      <p class="holder__title">Title</p>
    </div>

    <ul class="contact">
      <li class="contact__item">
        <svg class="contact__icon" viewBox="0 0 24 24"><path d="M6.6 10.8a15 15 0 0 0 6.6 6.6l2.2-2.2a1 1 0 0 1 1-.25 11.4 11.4 0 0 0 3.6.57 1 1 0 0 1 1 1V20a1 1 0 0 1-1 1A17 17 0 0 1 3 4a1 1 0 0 1 1-1h3.5a1 1 0 0 1 1 1c0 1.25.2 2.45.57 3.57a1 1 0 0 1-.25 1z"/></svg>
        <span>01632318257</span>
      </li>
      <li class="contact__item">
        <svg class="contact__icon" viewBox="0 0 24 24"><path d="M8 1h8a2 2 0 0 1 2 2v18a2 2 0 0 1-2 2H8a2 2 0 0 1-2-2V3a2 2 0 0 1 2-2zm0 3v8h8V4zm1 10v2h2v-2zm4 0v2h2v-2zm-4 3v2h2v-2zm4 0v2h2v-2z"/></svg>
        <span>07924168330</span>
      </li>
      <li class="contact__item">
        <svg class="contact__icon" viewBox="0 0 24 24"><path d="M2 6h20v13H2zm2 2v.5l8 5 8-5V8l-8 5z"/></svg>
        <span>info@velmorin.example</span>
      </li>
      <li class="contact__item">
        <svg class="contact__icon" viewBox="0 0 24 24"><path d="M12 2a10 10 0 1 0 0 20 10 10 0 0 0 0-20zm6.9 6h-3a15 15 0 0 0-1.3-3.9A8 8 0 0 1 18.9 8zM12 4c.8 1.2 1.5 2.5 1.9 4h-3.8c.4-1.5 1.1-2.8 1.9-4zM4.3 14a8 8 0 0 1 0-4h3.4a16 16 0 0 0 0 4zm.8 2h3a15 15 0 0 0 1.3 3.9A8 8 0 0 1 5.1 16zM8 8H5.1a8 8 0 0 1 4.3-3.9A15 15 0 0 0 8 8zm4 12c-.8-1.2-1.5-2.5-1.9-4h3.8c-.4 1.5-1.1 2.8-1.9 4zm2.3-6H9.7a14 14 0 0 1 0-4h4.6a14 14 0 0 1 0 4zm.3 5.9A15 15 0 0 0 15.9 16h3a8 8 0 0 1-4.3 3.9zM16.3 14a16 16 0 0 0 0-4h3.4a8 8 0 0 1 0 4z"/></svg>
        <span>www.velmorin.example</span>
      </li>
      <li class="contact__address">Piotr Velmorin 14 Pellham Birch Lane<br>Brackwell Cross,Hollshire,BX4 2QR</li>
    </ul>
  </section>

  <section class="card card--back">
    <div class="brand">
      <span class="brand__name">VELMORIN</span>
      <span class="brand__tagline">PROPERTY REFURBISHMENT &amp; MAINTENANCE</span>
    </div>
    <p class="card__web">www.velmorin.example</p>
  </section>

</div>
</body>
</html>
```